New start-up venture GlenTorvas needs eye-catching, bright, vibrant catering menu design.

GlenTorvas is looking for a tri-fold menu design (6 total pages) for our start-up catering business in Southern New Jersey. Designs should be informative, colorful, appealing, and represent the overall GlenTorvas concept:

“The vision of GLENTORVAS is to provide high quality organic nutrient dense food, juices, and snacks at affordable prices in a positive, fun, and educational environment inspiring a revolution of optimal health and well-being.”

Glentorvas is a Revolutionary catering/take-out concept offering a simple, customizable menu for customers who appreciate a modern approach to traditional food but also place a high priority on health, taste, affordability, and convenience.

Target Market(s)

Glentorvas primary market consists of on-the-go health conscious eaters and those with food allergies. They are deliberate about their eating choices, value quality and convenience, and are willing to pay more for those qualities. We provide Real Food for Real People in the rapidly growing segment of the health conscious dining industry.

Requirements
Must have
• The tri-fold (6 total pages) catering menu brochure must include our name and We Are GlenTorvas logo that has been attached.
You are free to pick and choose our personal pictures of salads, juices, snacks, etc. which are also attached.
The list of various GlenTorvas benefits on the back page of brochure (also added to the uploaded files).
Actual menu items and descriptions (uploaded file section)
Unique, easy to read (legible), fun, and eye-catching font. Please include the following saying, "Real Food for Real People"

Front cover (First page) should be the We Are GlenTorvas logo and space for contact information (You can choose to include pictures of various GlenTorvas, fruits, and vegetables or choose from our personal pictures that are attached)
Pages 2 through 5 should each include our various menu items - all information has been attached:
(Page 2 - Information/pictures with names and descriptions of the GlenTorva smoothies, Page 3 - Information/pictures on the Fresh organic juices with names and descriptions, Page 4 - Information/pictures on the Super Charged Salads with names and descriptions, Page 5 - Information/pictures on additional packaged and prepared menu items)
Page 6 (Back cover - the attached list of various GlenTorva benefits - maybe a picture of the We Are GlenTorvas spinner game - attached file)
Nice to have
• It would be nice for the brochure to incorporate the colors in the GlenTorvas seed of life logo and/or greens, oranges (colors of vegetables). Should you come across a stunning photograph that would benefit brochure, we would entertain that idea of including that photo.
Should not have
• Too much open or empty space.

```html
<!DOCTYPE html>
<html lang="en">
<head>
<meta charset="utf-8">
<title>We Are GlenTorvas – Tri-fold Menu</title>
<link href="https://fonts.googleapis.com/css2?family=Cinzel:wght@400&family=Lato:ital,wght@0,300;0,400;0,700;1,700&display=swap" rel="stylesheet">
<style>
:root{
  --brown:#4a3426;
  --lime:#9cc31a;
  --lime-soft:#d6e8a0;
  --green-text:#8dc021;
  --ink:#333333;
  --paper:#ffffff;
}
*{margin:0;padding:0;box-sizing:border-box}
html,body{width:896px;height:1200px;overflow:hidden;background:var(--paper)}
body{position:relative;font-family:"Lato",Arial,sans-serif;color:#fff}
.sheet{position:absolute;left:0;width:896px;height:600px;overflow:hidden}
.sheet--outside{top:0}
.sheet--inside{top:600px}
.pattern{position:absolute;inset:0;width:100%;height:100%}
.panel{position:absolute;background:var(--brown);border-radius:8px;overflow:hidden;padding:10px 9px}
.panel p,.panel li{font-size:6.9px;line-height:1.4}
.panel p{margin-bottom:7px}
.panel b{font-weight:700}
.panel--extras p{margin-bottom:10px}
.menu-head{height:58px;display:flex;flex-direction:column;align-items:center;justify-content:flex-end;margin-bottom:12px}
.menu-head h2{font-family:"Cinzel",serif;font-weight:400;font-size:13px;letter-spacing:.5px;color:#fff;padding:0 8px 2px;border-bottom:1px solid #fff;position:relative}
.menu-head h2::before,.menu-head h2::after{content:"";position:absolute;bottom:-1px;width:22px;border-bottom:1px solid #fff}
.menu-head h2::before{left:-26px}
.menu-head h2::after{right:-26px}
.menu-head .crest{width:34px;height:16px;border:1px solid #fff;border-bottom:none;border-radius:17px 17px 0 0;margin-bottom:6px}
.photo{position:absolute;left:0;right:0;bottom:0}
.brand{position:absolute;text-align:center;color:#222;font-family:"Lato",Arial,sans-serif;font-weight:300}
.brand .we{display:block}
.brand .name{display:inline-flex;align-items:center;gap:6px}
.brand .dot{display:inline-block;border-radius:50%;background:var(--lime)}
.tagline{position:absolute;font-family:"Lato",Arial,sans-serif;font-style:italic;font-weight:700;color:var(--green-text)}
.benefits{position:absolute;left:315px;top:183px;width:266px;height:229px;background:var(--brown);border-radius:6px;padding:8px 8px}
.benefits h3{font-size:7px;font-weight:700;margin-bottom:6px}
.benefits ul{list-style:none;display:grid;grid-template-columns:1fr 1fr;column-gap:6px;row-gap:7px}
.benefits li{font-size:6.6px;line-height:1.35;padding-left:5px;text-indent:-5px}
.benefits li::before{content:"• "}
.build{display:grid;grid-template-columns:1fr 1fr;gap:4px;margin-bottom:6px}
.build h4{font-size:5.8px;font-weight:700;margin-bottom:1px}
.build ul{list-style:none;columns:3;column-gap:3px}
.build li{font-size:5.8px;line-height:1.3}
.build .dry ul{columns:2}
</style>
</head>
<body>

<section class="sheet sheet--outside">
  <svg class="pattern" viewBox="0 0 896 600" role="img" aria-label="Green gingham check pattern">
    <defs>
      <linearGradient id="gingham" x1="0" y1="0" x2="1" y2="1">
        <stop offset="0" stop-color="#b5d44a"/>
        <stop offset="1" stop-color="#d6e8a0"/>
      </linearGradient>
    </defs>
    <polygon points="470,0 896,0 896,60 810,175 395,175" fill="url(#gingham)"/>
    <polygon points="395,425 896,425 896,590 600,590" fill="url(#gingham)"/>
    <polygon points="0,240 24,265 24,320 0,345" fill="url(#gingham)"/>
  </svg>

  <article class="panel panel--extras" style="left:25px;top:25px;width:265px;height:547px">
    <header class="menu-head"><span class="crest"></span><h2>ADDITIONAL MENU</h2></header>
    <p><b>Additional Packaged Menu Items:</b></p>
    <p><b>Trailwise Bars and Granola Cereals</b></p>
    <p><b>GlenTorva Cereals</b></p>
    <p><b>Fairmeadow Multi-Grain and Sweet Potato Chips</b></p>
    <p><b>Early Tide Sea Salt and Twilight Berry Chips</b></p>
    <p><b>Verdant Start Greens and Chocolate Energy Bars</b></p>
    <p><b>Northmark Nut Clusters</b></p>
    <p><b>Additional Prepared Menu Items:</b></p>
    <p><b>Quinoa with Zucchini and Squash.</b> Prepared in olive oil, with pepperoncini and various spices</p>
    <p><b>Lean ground Turkey meat quinoa tacos.</b> Prepared in olive oil with pepperoncini and various spices</p>
    <div class="photo" role="img" aria-label="Stack of multi-grain and sweet potato chips" style="height:255px;background:linear-gradient(135deg,#d9a24a 0%,#e8c98a 35%,#6b4a6e 60%,#d48a2c 100%)"></div>
  </article>

  <aside class="benefits">
    <h3>GlenTorva Benefits</h3>
    <ul>
      <li>Both a food and medicine</li>
      <li>Superior source of anti-oxidants</li>
      <li>Nutrient dense and calorie sparse</li>
      <li>No known negative properties or side effects</li>
      <li>Protects and Heals the Body</li>
      <li>Increases Energy</li>
      <li>Improves Overall Health</li>
      <li>Nourishes the Entire Body</li>
      <li>Increases Life Expectancy</li>
      <li>Reduce Body Fat</li>
      <li>Boosts Mood</li>
      <li>Reduces Stress</li>
      <li>Aids Digestion</li>
      <li>Improves Productivity</li>
      <li>Corrects Imbalances</li>
      <li>Reduces Inflammation</li>
      <li>Boosts and Supports the Immune System</li>
      <li>Prevents and Reverses Chronic Disease</li>
      <li>Slows Down the Aging Process</li>
      <li>Improves the severity and symptoms of major diseases</li>
      <li>Cleanses and Detoxifies the Body</li>
    </ul>
  </aside>

  <div class="brand" style="left:320px;top:458px;width:260px">
    <span class="we" style="font-size:31px;line-height:1.1">We Are</span>
    <span class="name" style="font-size:29px"><span>GLENTORVAS</span><span class="dot" style="width:14px;height:14px"></span></span>
  </div>

  <div class="brand" style="left:610px;top:258px;width:270px">
    <span class="we" style="font-size:32px;line-height:1.1">We Are</span>
    <span class="name" style="font-size:30px"><span>GLENTORVAS</span><span class="dot" style="width:14px;height:14px"></span></span>
  </div>
  <p class="tagline" style="left:610px;top:343px;width:270px;text-align:center;font-size:14px">Real Food for Real People</p>
</section>

<section class="sheet sheet--inside">
  <svg class="pattern" viewBox="0 0 896 600" role="img" aria-label="Green gingham check pattern">
    <defs>
      <linearGradient id="gingham2" x1="0" y1="0" x2="0" y2="1">
        <stop offset="0" stop-color="#b5d44a"/>
        <stop offset="1" stop-color="#d6e8a0"/>
      </linearGradient>
    </defs>
    <rect x="0" y="8" width="896" height="575" fill="url(#gingham2)"/>
  </svg>

  <article class="panel" style="left:25px;top:28px;width:265px;height:547px">
    <header class="menu-head"><span class="crest"></span><h2>SMOOTHIES MENU</h2></header>
    <p><b>GlenTorva Smoothies :-</b> Blendcore frozen fruit plant based protein smoothies:</p>
    <p><b>Vanilla Vortex –</b> Frozen fruits include strawberries, pineapple, peaches, mango, and blueberries, Vanilla almond milk, Spirulina Vanilla protein powder, and Vanilla Blueberry Trailwise granola clusters</p>
    <p><b>Strawberry Tsunami</b> - Frozen fruits include strawberries, pineapple, peaches, mango, and blueberries, vanilla coconut milk, Spirulina Strawberry protein powder, and Oat &amp; Honey Trailwise granola clusters</p>
    <p><b>Chocolate Cyclone</b> - Frozen fruits include strawberries, pineapple, peaches, mango, and blueberries, Chocolate almond milk, Spirulina Chocolate protein powder, and Dark Chocolate &amp; Cranberry Trailwise granola clusters</p>
    <p><b>Vanilla Chai Clear Blue Sky</b> - Frozen fruits include strawberries, pineapple, peaches, mango, and blueberries, Vanilla almond/coconut milk blend, Verano Vanilla chai protein powder, and Cinnamon Oat Trailwise granola clusters</p>
    <p><b>Build your own Smoothie:</b> Choice of frozen fruits include strawberries, pineapple, peaches, mango, blueberries, kiwi, and grapes.</p>
    <p>Choice of plant based, Non-GMO protein powders include Vanilla, Strawberry, and Chocolate Spirulina, Vanilla and Chocolate Sunstrider Raw Protein blend, Verano Chai Verano One Nutritional Shake, and Orchard Path Raw Organic Vanilla Protein</p>
    <p>Choice of non-dairy milk alternatives include Vanilla &amp; Chocolate Almond (Sweetened and Unsweetened), Vanilla coconut milk, Vanilla &amp; Chocolate Rice milk, and Vanilla quinoa milk</p>
    <p>Choice of Trailwise Granola Clusters include Vanilla Blueberry Clusters, Dark Chocolate &amp; Cranberry Clusters, Maple Walnut Clusters with Chia &amp; Quinoa, and Peanut butter Whole Grain Clusters.</p>
    <p><b>GlenTorva Me Optional Items:</b> Decadent Blend - Chia and Flax Seed with Coconut and Cacoa</p>
    <div class="photo" role="img" aria-label="Pink berry smoothie in a glass with a striped straw" style="height:140px;background:linear-gradient(160deg,#f6b8d4 0%,#d9287e 45%,#8a1a54 100%)"></div>
  </article>

  <article class="panel" style="left:315px;top:28px;width:266px;height:547px">
    <header class="menu-head"><span class="crest"></span><h2>ORGANIC JUICE MENU</h2></header>
    <p><b>Fresh Organic Juices:</b></p>
    <p><b>Awakening</b> – Fresh organic blend of Apples, Carrots, and Celery</p>
    <p><b>Illuminator</b> – Fresh organic blend of Apples, Carrots, Celery, and Kale</p>
    <p><b>Enlightenment</b> – Fresh organic blend of Apples, Carrots, and Beets</p>
    <p><b>Ascension</b> - Fresh organic blend of Apples, Carrots, Celery, Lemon, and Ginger root</p>
    <p><b>Longevity</b> – Fresh organic blend of Apples, Carrots, Greens, and Ruby Crest goji blend</p>
    <p style="margin-top:14px"><b>GlenTorva-Me Optional Items:</b></p>
    <p>Aloe Vera water</p>
    <p>Chia seeds</p>
    <p>Spirulina</p>
    <p>Ruby Crest Goji Berry blend</p>
    <div class="photo" role="img" aria-label="Row of colourful fresh juices in tall glasses" style="height:255px;background:linear-gradient(90deg,#e0442a 0%,#f3a0b8 30%,#6b4a38 55%,#d98a3c 78%,#f2d7b0 100%)"></div>
  </article>

  <article class="panel" style="left:606px;top:28px;width:266px;height:547px">
    <header class="menu-head"><span class="crest"></span><h2>SALAD MENU</h2></header>
    <p><b>Super Charged Salads:</b></p>
    <p><b>Salad #1: Carb Buster</b> - Dark leafy greens mix AKA:"secret stock", asparagus, green beans, broccoli, cauliflower, green apple, spinach, peppers, cucumber, citrus zest, lemon splash and nuts.</p>
    <p><b>Salad #2: Fruit Delight</b> - Dark leafy greens mix, diced mango, berry assortment, sprouts, carrots, organic raisins or craisins (customer choice).</p>
    <p><b>Salad #3: Mental Clarity/ Energizer</b> - Spinach, Bok Choy, tri-colored bell peppers, beets, blue berries, cabbage duo, orange slices, jicama and sweet potato wedges. Served with savory smooth Turmeric dressing.* Turmeric promotes brain cell stimulation.</p>
    <p><b>Salad #4: The Diabetic's Friend</b> - Dark leafy greens mix, broccoli, cabbage, cauliflower, tomato, avocado, cucumber, onion, spinach, watercress greens, flax, pumpkin and sunflower seeds, beans, nuts and herbs:(cilantro,oregano,basil,mint mixture). This specialty Super Charged Salad comes with a side topping of cinnamon sprinkled apples with musli granola.</p>
    <p><b>Salad #5: Massaged Kale Protein Booster</b> - Kale, edemamme(soy beans), chick peas, finely chopped green beans, dried cherries, sliced almonds, celery leaves, parsley, black beans. This beauty of goodness is served on a layer of spinach leaves.</p>
    <p style="margin-bottom:2px"><b>Build Your Own Super Charged Salad:</b></p>
    <div class="build">
      <div>
        <h4>Base ingredients:</h4>
        <ul>
          <li>• Asparagus</li><li>• Arugula</li><li>• Avocado</li><li>• Beets</li><li>• Blueberries</li><li>• Broccoli</li>
          <li>• Carrots</li><li>• Jicama</li><li>• Kale</li><li>• Mushrooms</li><li>• Olives</li><li>• Onions</li>
          <li>• Radishes</li><li>• Romaine</li><li>• Spinach</li><li>• Sprouts</li><li>• Tomatoes</li><li>• Watercress</li>
        </ul>
      </div>
      <div class="dry">
        <h4>Dry ingredients:</h4>
        <ul>
          <li>Chia Seeds</li><li>Craisins</li><li>Ground Flax</li><li>Goji Berries</li><li>Hemp Seeds</li><li>Pumpkin Seeds</li>
          <li>Sunflower Seeds</li><li>Walnuts</li><li>Pecans</li><li>Almonds</li>
        </ul>
      </div>
    </div>
    <p><b>Choice of salad dressings:</b> Balsamic Vinaigrette, Vidalia onion, Ranch</p>
    <div class="photo" role="img" aria-label="Large bowl of fresh chopped green salad" style="height:150px;background:radial-gradient(ellipse at 50% 45%,#7fae3a 0%,#c9a24e 45%,#a86a2e 65%,#f1ece4 90%)"></div>
  </article>
</section>

</body>
</html>
```